Halvorsen & Tate Client Brochure

I need a Tri- fold brochure for a Custom cabinet company who has first rate skilled millworkers who custom craft cabinets from kitchens, bathrooms, living room entertainment centers, bedrooms to beautiful custom library's, fireplace mantels as well as garages and basement storage units and shelves. They also have a large selection of in stock mouldings. The company has been in business since 1943.See New logo, photos along with old business card and lets create brochure that's fresh and exciting.

Target Market(s)

Homeowners

Industry/Entity Type

It Company

Requirements
Must have
• Company Logo, Business Address, clear photos etc
Nice to have
• Clean and professional looking brochure.

```html
<!DOCTYPE html>
<html lang="en">
<head>
<meta charset="utf-8">
<title>Halvorsen &amp; Tate – Tri-fold Brochure</title>
<link href="https://fonts.googleapis.com/css2?family=Teko:wght@400;500;600&family=Lato:wght@400;700&display=swap" rel="stylesheet">
<style>
:root{
  --gold:#c9a13b;
  --gold-light:#ecd383;
  --gold-deep:#a67c22;
  --charcoal:#3a3a3c;
  --paper:#f5f5f5;
  --ink:#262626;
  --backdrop:#eeeeee;
}
*{margin:0;padding:0;box-sizing:border-box}
html,body{width:1200px;height:1200px;overflow:hidden}
body{background:var(--backdrop);font-family:"Lato",sans-serif;color:var(--ink);position:relative}
.sheet{position:absolute;left:250px;width:700px;height:500px;background:var(--paper);overflow:hidden}
.sheet--outside{top:92px}
.sheet--inside{top:614px}
.sheet svg.art{position:absolute;inset:0}
.abs{position:absolute}
.label{font-family:"Teko",sans-serif;font-weight:400;color:var(--gold);text-transform:uppercase;letter-spacing:.2px;line-height:1}
.list{list-style:none;font-size:7.6px;line-height:14.6px}
.list li::before{content:"";display:inline-block;width:4px;height:4px;border-radius:50%;background:var(--gold);margin-right:4px;vertical-align:1px}
.on-dark{color:#fff}
.showroom-tab{left:60px;top:382px;width:120px;height:40px;background:var(--charcoal);border-radius:8px 8px 0 0;color:#fff;font-size:10.5px;line-height:12px;text-align:center;padding-top:7px;box-shadow:0 2px 4px rgba(0,0,0,.3)}
.showroom-box{left:14px;top:388px;width:208px;height:76px;border-radius:6px;background:linear-gradient(180deg,var(--gold-light),var(--gold) 55%,var(--gold-deep))}
.showroom-lines{left:14px;top:429px;width:208px;text-align:center;color:var(--charcoal);font-size:11px;line-height:17px}
.showroom-lines small{font-size:9.5px}
.address{left:0;top:472px;width:238px;text-align:center;font-size:7.5px}
.quote-top{left:290px;top:34px;width:163px;text-align:right;font-size:7.5px;line-height:10px;color:var(--ink)}
.contact{left:290px;top:360px;width:170px;text-align:right;color:#fff}
.contact .label{font-family:"Lato",sans-serif;font-size:11.5px;line-height:14px;margin-bottom:4px;text-transform:none}
.contact p{font-size:11.5px;line-height:19px;white-space:nowrap}
.contact p.small{font-size:8.5px;line-height:18px}
.ico{display:inline-block;width:8px;height:7px;border:1.2px solid var(--gold);border-radius:1px;margin-left:6px;vertical-align:0}
.socials{left:290px;top:467px;width:170px;text-align:right;color:#fff;font-size:7px}
.socials span::before{content:"";display:inline-block;width:8px;height:8px;border-radius:50%;background:var(--gold);margin:0 3px 0 6px;vertical-align:-1px}
.brand{left:469px;top:40px;width:231px;text-align:center;color:var(--gold);font-family:"Lato",sans-serif;font-weight:700;font-size:16px;line-height:20px}
.brand-mark{display:block;width:22px;height:22px;border-radius:50%;background:var(--gold);margin:0 auto 8px}
.headline{left:469px;top:412px;width:231px;text-align:center}
.headline .pre{font-family:"Teko",sans-serif;font-weight:600;font-size:21px;line-height:18px;color:var(--charcoal)}
.headline .main{font-family:"Teko",sans-serif;font-weight:600;font-size:31px;line-height:28px;color:var(--gold)}
.headline .post{font-size:8.5px;color:var(--ink);margin-top:2px}
.family{left:22px;top:244px;width:216px;font-weight:700;font-size:12.5px;line-height:15px;color:var(--ink)}
.reviews-title{left:0;top:284px;width:238px;text-align:center;color:#fff;font-size:12px}
.review{left:22px;width:206px;text-align:justify;text-align-last:center;font-size:7.3px;line-height:9.6px;color:var(--ink)}
.review::before{content:"\201C";font-weight:700;font-size:10px}
.review::after{content:"\201D";font-weight:700;font-size:10px}
.suppliers-title{left:259px;top:24px;width:205px;font-size:17px;line-height:20px;color:var(--gold-deep);white-space:nowrap}
.suppliers{left:262px;top:74px;display:grid;grid-template-columns:97px 110px;font-size:8.6px;line-height:17px}
.suppliers li::before{content:"";display:inline-block;width:5px;height:5px;border-radius:50%;background:var(--gold);margin-right:5px;vertical-align:1px}
.suppliers ul{list-style:none}
</style>
</head>
<body>

<section class="sheet sheet--outside">
  <svg class="art" width="700" height="500" viewBox="0 0 700 500">
    <defs>
      <linearGradient id="goldFill" x1="0" y1="0" x2="1" y2="1">
        <stop offset="0" stop-color="#f0d98b"/><stop offset=".5" stop-color="#c9a13b"/><stop offset="1" stop-color="#9c741d"/>
      </linearGradient>
      <linearGradient id="mist" x1="0" y1="0" x2="1" y2="0">
        <stop offset="0" stop-color="#e4e4e4"/><stop offset="1" stop-color="#fafafa"/>
      </linearGradient>
      <linearGradient id="showroomTone" x1="0" y1="0" x2="1" y2="1">
        <stop offset="0" stop-color="#eae6df"/><stop offset=".55" stop-color="#c9b89a"/><stop offset="1" stop-color="#8e2f35"/>
      </linearGradient>
      <linearGradient id="storefrontTone" x1="0" y1="0" x2="0" y2="1">
        <stop offset="0" stop-color="#d9d4ce"/><stop offset="1" stop-color="#6d6a68"/>
      </linearGradient>
      <linearGradient id="counterTone" x1="0" y1="0" x2="0" y2="1">
        <stop offset="0" stop-color="#dfe1e3"/><stop offset="1" stop-color="#3b4250"/>
      </linearGradient>
    </defs>
    <path d="M0,0H238V205C170,172 80,145 0,142Z" fill="var(--charcoal)"/>
    <path d="M0,142C80,145 170,172 238,205V218C170,190 80,162 0,160Z" fill="url(#goldFill)"/>
    <circle cx="64" cy="140" r="44" fill="url(#storefrontTone)" stroke="var(--gold)" stroke-width="3" role="img" aria-label="Photo of the showroom storefront"/>
    <circle cx="158" cy="148" r="44" fill="url(#counterTone)" stroke="var(--gold)" stroke-width="3" role="img" aria-label="Photo of dark custom kitchen cabinets"/>
    <rect x="238" y="0" width="231" height="500" fill="url(#mist)"/>
    <path d="M238,0H248C262,130 320,215 400,262C320,240 262,200 238,170Z" fill="var(--charcoal)"/>
    <path d="M248,0C262,130 320,215 400,262" fill="none" stroke="var(--gold)" stroke-width="3"/>
    <path d="M250,500C280,385 330,300 400,262L469,262V500Z" fill="var(--charcoal)"/>
    <path d="M250,500C280,385 330,300 400,262" fill="none" stroke="var(--gold)" stroke-width="3"/>
    <rect x="469" y="0" width="231" height="262" fill="var(--charcoal)"/>
    <rect x="469" y="262" width="231" height="238" fill="#e6e6e6"/>
    <rect x="469" y="494" width="231" height="6" fill="var(--gold)"/>
    <path d="M342,262Q520,110 700,126V394Q520,410 342,262Z" fill="url(#showroomTone)" stroke="var(--gold)" stroke-width="5" role="img" aria-label="Photo of the moulding showroom with shelves of samples"/>
    <path d="M238,215C300,240 330,258 342,262" fill="none" stroke="var(--gold)" stroke-width="4"/>
    <circle cx="398" cy="132" r="50" fill="url(#goldFill)" stroke="var(--charcoal)" stroke-width="3"/>
    <circle cx="398" cy="132" r="45" fill="none" stroke="var(--gold-light)" stroke-width="1"/>
    <text x="398" y="141" text-anchor="middle" font-family="Lato, sans-serif" font-weight="700" font-size="31" fill="var(--charcoal)">FREE</text>
    <text x="398" y="160" text-anchor="middle" font-family="Lato, sans-serif" font-size="13" fill="var(--charcoal)">ESTIMATES</text>
  </svg>

  <p class="abs label" style="left:15px;top:27px;font-size:11px">We offer:</p>
  <ul class="abs list on-dark" style="left:15px;top:40px">
    <li>Over 75 years experience</li><li>Real wood Construction</li><li>Manufactured on site</li>
  </ul>
  <ul class="abs list on-dark" style="left:126px;top:40px">
    <li>Free cabinet design</li><li>Free estimates</li><li>Free samples</li>
  </ul>

  <p class="abs label" style="left:14px;top:196px;font-size:11px">Cabinets</p>
  <ul class="abs list" style="left:14px;top:207px">
    <li>Kitchen</li><li>Bath</li><li>Libraries</li><li>Office</li><li>Entertainment Centers</li>
  </ul>
  <ul class="abs list" style="left:120px;top:205px;line-height:10px">
    <li style="margin-bottom:5px">Fireplace Mantels</li><li style="margin-bottom:5px">Garage &amp; Basement<br>&nbsp;&nbsp;&nbsp;Shelving</li><li>Storage units</li>
  </ul>
  <p class="abs label" style="left:14px;top:290px;font-size:11px">Mouldings</p>
  <ul class="abs list" style="left:14px;top:300px">
    <li>Over 200 Mouldings in stock</li><li>Custom match mouldings</li><li>Base</li><li>Crown</li>
  </ul>
  <ul class="abs list" style="left:132px;top:300px">
    <li>Ceiling &amp; many more</li><li>Columns</li><li>Corbels</li>
  </ul>

  <div class="abs showroom-box"></div>
  <div class="abs showroom-tab">COME VISIT<br>OUR SHOWROOM</div>
  <div class="abs showroom-lines">
    <span class="ico" style="margin:0 3px 0 0;border-color:var(--charcoal)"></span>555-010-4821 &nbsp;<span class="ico" style="margin:0 3px 0 0;border-color:var(--charcoal)"></span>555-010-4822<br>
    <small>sales@halvorsentate.com</small>
  </div>
  <p class="abs address">218 alder row, bayfield ca 94000</p>

  <p class="abs label" style="left:290px;top:22px;width:163px;text-align:right;font-size:9.5px">Quality, Reliability, Value</p>
  <p class="abs quote-top">We take time to understand our customer's expectations. Customer service is more than just a trendy theme. It's the underlying philosophy in everything we do.</p>

  <div class="abs contact">
    <p class="label" style="color:var(--gold)">Conatct us</p>
    <p>555-010-4821<span class="ico"></span></p>
    <p>555-010-4822<span class="ico"></span></p>
    <p class="small">sales@halvorsentate.com<span class="ico"></span></p>
    <p class="small">www.halvorsentate.com<span class="ico" style="border-radius:50%"></span></p>
  </div>
  <p class="abs socials"><span>Neighborly</span><span>Ratewise</span><span>Circlet</span></p>

  <div class="abs brand">
    <span class="brand-mark"></span>
    Halvorsen &amp; Tate
  </div>

  <div class="abs headline">
    <p class="pre">YOUR PLACE FOR ALL WOOD</p>
    <p class="main">CUSTOM CABINETS</p>
    <p class="post">AND 100'S OF MOULDINGS ALL IN STOCK</p>
  </div>
</section>

<section class="sheet sheet--inside">
  <svg class="art" width="700" height="500" viewBox="0 0 700 500">
    <defs>
      <linearGradient id="goldFill2" x1="0" y1="0" x2="1" y2="1">
        <stop offset="0" stop-color="#f0d98b"/><stop offset=".5" stop-color="#c9a13b"/><stop offset="1" stop-color="#9c741d"/>
      </linearGradient>
      <linearGradient id="woodKitchen" x1="0" y1="0" x2="0" y2="1">
        <stop offset="0" stop-color="#c99c64"/><stop offset=".5" stop-color="#b9b6b0"/><stop offset="1" stop-color="#8a5f33"/>
      </linearGradient>
      <linearGradient id="islandTone" x1="0" y1="0" x2="1" y2="1">
        <stop offset="0" stop-color="#e8e4dc"/><stop offset=".3" stop-color="#8e98a0"/><stop offset="1" stop-color="#4d5760"/>
      </linearGradient>
      <linearGradient id="whiteKitchen" x1="0" y1="0" x2="0" y2="1">
        <stop offset="0" stop-color="#ecebe8"/><stop offset=".6" stop-color="#a3826a"/><stop offset="1" stop-color="#3f2f25"/>
      </linearGradient>
      <linearGradient id="closetTone" x1="0" y1="0" x2="1" y2="0">
        <stop offset="0" stop-color="#d8d6d2"/><stop offset=".6" stop-color="#f1f1ef"/><stop offset="1" stop-color="#c9cbcc"/>
      </linearGradient>
      <linearGradient id="hallTone" x1="0" y1="0" x2="0" y2="1">
        <stop offset="0" stop-color="#e6e3de"/><stop offset="1" stop-color="#9b958d"/>
      </linearGradient>
      <linearGradient id="diningTone" x1="0" y1="0" x2="0" y2="1">
        <stop offset="0" stop-color="#d9c2a0"/><stop offset="1" stop-color="#8a3a2e"/>
      </linearGradient>
    </defs>
    <rect x="0" y="0" width="238" height="215" fill="url(#woodKitchen)" role="img" aria-label="Photo of a natural wood kitchen with range hood"/>
    <path d="M0,205C80,188 170,188 238,210V500H0Z" fill="url(#goldFill2)"/>
    <path d="M0,205C80,188 170,188 238,210" fill="none" stroke="var(--gold-light)" stroke-width="2"/>
    <rect x="238" y="0" width="231" height="500" fill="#fff"/>
    <path d="M238,500V330C300,280 400,250 469,210V500Z" fill="var(--charcoal)"/>
    <path d="M238,330C300,280 400,250 469,210" fill="none" stroke="var(--gold)" stroke-width="3"/>
    <path d="M228,500C260,420 330,350 440,315C455,312 462,305 469,300V500Z" fill="url(#whiteKitchen)" role="img" aria-label="Photo of a white kitchen with range and stone backsplash"/>
    <path d="M228,500C260,420 330,350 440,315" fill="none" stroke="var(--gold)" stroke-width="3"/>
    <path d="M258,190L390,165L470,200L455,270L420,335L272,282Z" fill="url(#islandTone)" role="img" aria-label="Photo of a grey kitchen island with turned leg"/>
    <rect x="469" y="0" width="231" height="500" fill="url(#goldFill2)"/>
    <path d="M430,500V200C520,200 620,175 700,140V500Z" fill="url(#closetTone)" role="img" aria-label="Photo of white built-in wardrobe cabinets and glass shower"/>
    <path d="M430,200C520,200 620,175 700,140" fill="none" stroke="var(--gold)" stroke-width="4"/>
    <circle cx="538" cy="120" r="58" fill="url(#hallTone)" stroke="var(--gold)" stroke-width="3" role="img" aria-label="Photo of a hallway lined with built-in cabinets"/>
    <circle cx="646" cy="94" r="46" fill="url(#diningTone)" stroke="var(--gold)" stroke-width="3" role="img" aria-label="Photo of a wood-panelled dining room"/>
  </svg>

  <p class="abs family">Halvorsen &amp; Tate Family owned<br>since 1943</p>
  <p class="abs label reviews-title">Ratewise Reviews</p>
  <p class="abs review" style="top:305px">Great family owned business with friendly staff. Very accommodating to satisfy your needs. Great quality! Would highly recommend them!</p>
  <p class="abs review" style="top:354px">This is the only place I would ever recommend for custom cabinetry. I have many pieces of their work here in my home from a mantel, to a bed-room set, a entertainment cabinet, bookshelves, and my newest addition my gorgeous kitchen. I have been using them for many years.</p>
  <p class="abs review" style="top:434px">We love the craftsmen and owners at this won-derful cabinet shop. We have worked with the family many times over the past 15 years to help us create and build cabinets.</p>

  <p class="abs label suppliers-title">We are able to get any products from<br>these companies within days</p>
  <div class="abs suppliers">
    <ul><li>Kestrel Mill</li><li>Northgate Trim</li><li>Silver Creek</li></ul>
    <ul><li>Elm &amp; Ash</li><li>Spindlecraft Columns</li><li>Fairlon</li></ul>
  </div>
</section>

</body>
</html>
```